Verpackung: 5 cm breites Klebeband für Kartons
Zielgruppe
Wir verkaufen Stoffe Meterware.
Stoffe zum Polstern, für Kissenbezüge, für Gardinen oder für Vorhänge zum Abdunkeln.
Wichtig für uns ist eine gute Qualität und schöne, moderne Stoffe.
Aufgabenstellung
Es soll ein Klebeband bedruckt werden, das muss designt werden. Das Klebeband ist 5 cm breit und transparent.
Es soll einen farbigen Hintergrund geben, Farbe egal.
Die Schrift sollte nur in einer Farbe sein.
Wichtig ist, dass die Hintergund- + Schirftfarbe zu dieser typischen braunen Kartonage passen. Also ein weißer Hintergrund finden wir sticht zu sehr ab von dem Braun. Als Hintergrund können wir uns Beige, Grau oder eine ähnliche Richtung ... vorstellen.
Das Logo sollte darauf platziert sein. Und die www-Adresse. www.tuchwelt.de - es kann gerne auch mehr sein, Hauptsache es sieht gut aus!!
Gut heißt für uns, schön, aufgeräumt, schlicht modern.

```html
<!DOCTYPE html>
<html lang="de">
<head>
<meta charset="utf-8">
<title>tuchwelt.de – Klebeband Farbvarianten</title>
<link rel="stylesheet" href="https://fonts.googleapis.com/css2?family=EB+Garamond&family=Quicksand:wght@400;500&family=Ubuntu:wght@400;500&display=swap">
<style>
  :root {
    --page: #ffffff;
    --ink: #1c1a1a;
    --mark: #444444;
    --a-light: #fee6b8; --a-dark: #fddea0; --a-url: #d46a00;
    --b-light: #fee6b8; --b-dark: #fddea0; --b-url: #8a7862;
    --c-light: #f1dcc7; --c-dark: #e9cbab; --c-url: #c98240;
    --d-light: #ddd3c6; --d-dark: #cfc4b4; --d-url: #9f8563;
    --e-light: #d6d6d6; --e-dark: #c6c6c6; --e-url: #686868;
  }
  * { box-sizing: border-box; margin: 0; padding: 0; }
  html, body { width: 848px; height: 1200px; overflow: hidden; background: var(--page); }
  .sheet { position: relative; width: 848px; height: 1200px; }
  .variant-label {
    position: absolute; left: 26px;
    font: 15px "EB Garamond", serif; color: var(--ink);
  }
  .tape {
    position: absolute; left: 20px; width: 808px; height: 202px; overflow: hidden;
    background: repeating-linear-gradient(135deg,
      var(--light) 0 62px, var(--dark) 62px 124px);
  }
  .tape--a { --light: var(--a-light); --dark: var(--a-dark); --url: var(--a-url); }
  .tape--b { --light: var(--b-light); --dark: var(--b-dark); --url: var(--b-url); }
  .tape--c { --light: var(--c-light); --dark: var(--c-dark); --url: var(--c-url); }
  .tape--d { --light: var(--d-light); --dark: var(--d-dark); --url: var(--d-url); }
  .tape--e { --light: var(--e-light); --dark: var(--e-dark); --url: var(--e-url); }
  .url-row {
    position: absolute; left: 16px; right: 26px;
    display: flex; justify-content: space-between; white-space: nowrap;
    font: 500 13.5px "Ubuntu", sans-serif; color: var(--url);
  }
  .url-row--top { top: 5px; }
  .url-row--bottom { bottom: 5px; left: 21px; right: 22px; }
  .url-row .sep { padding: 0 2px; }
  .brand { position: absolute; left: 163px; top: 66px; width: 460px; height: 90px; }
  .brand-square {
    position: absolute; left: 0; top: 14px; width: 58px; height: 58px;
    background: var(--mark); border-radius: 5px;
  }
  .brand-name {
    position: absolute; left: 103px; top: -8px;
    font: 400 60px/1 "Quicksand", sans-serif; color: var(--ink); letter-spacing: -0.5px;
  }
  .brand-tagline {
    position: absolute; left: 104px; top: 56px;
    font: 400 17.5px/1 "Quicksand", sans-serif; color: var(--ink);
  }
</style>
</head>
<body>
<main class="sheet">

  <p class="variant-label" style="top:10px">a)</p>
  <section class="tape tape--a" style="top:39px">
    <div class="url-row url-row--top"><span>www.tuchwelt.de</span><span class="sep">·</span><span>www.tuchwelt.de</span><span class="sep">·</span><span>www.tuchwelt.de</span><span class="sep">·</span><span>www.tuchwelt.de</span><span class="sep">·</span><span>www.tuchwelt.de</span><span class="sep">·</span><span>www.tuchwelt.de</span><span class="sep">·</span></div>
    <div class="brand"><span class="brand-square"></span><p class="brand-name">tuchwelt.de</p><p class="brand-tagline">Stoffe für Wohnen, Hobby &amp; Design</p></div>
    <div class="url-row url-row--bottom"><span>www.tuchwelt.de</span><span class="sep">·</span><span>www.tuchwelt.de</span><span class="sep">·</span><span>www.tuchwelt.de</span><span class="sep">·</span><span>www.tuchwelt.de</span><span class="sep">·</span><span>www.tuchwelt.de</span><span class="sep">·</span><span>www.tuchwelt.de</span><span class="sep">·</span></div>
  </section>

  <p class="variant-label" style="top:241px">b)</p>
  <section class="tape tape--b" style="top:264px">
    <div class="url-row url-row--top"><span>www.tuchwelt.de</span><span class="sep">·</span><span>www.tuchwelt.de</span><span class="sep">·</span><span>www.tuchwelt.de</span><span class="sep">·</span><span>www.tuchwelt.de</span><span class="sep">·</span><span>www.tuchwelt.de</span><span class="sep">·</span><span>www.tuchwelt.de</span><span class="sep">·</span></div>
    <div class="brand"><span class="brand-square"></span><p class="brand-name">tuchwelt.de</p><p class="brand-tagline">Stoffe für Wohnen, Hobby &amp; Design</p></div>
    <div class="url-row url-row--bottom"><span>www.tuchwelt.de</span><span class="sep">·</span><span>www.tuchwelt.de</span><span class="sep">·</span><span>www.tuchwelt.de</span><span class="sep">·</span><span>www.tuchwelt.de</span><span class="sep">·</span><span>www.tuchwelt.de</span><span class="sep">·</span><span>www.tuchwelt.de</span><span class="sep">·</span></div>
  </section>

  <p class="variant-label" style="top:466px">c)</p>
  <section class="tape tape--c" style="top:489px">
    <div class="url-row url-row--top"><span>www.tuchwelt.de</span><span class="sep">·</span><span>www.tuchwelt.de</span><span class="sep">·</span><span>www.tuchwelt.de</span><span class="sep">·</span><span>www.tuchwelt.de</span><span class="sep">·</span><span>www.tuchwelt.de</span><span class="sep">·</span><span>www.tuchwelt.de</span><span class="sep">·</span></div>
    <div class="brand"><span class="brand-square"></span><p class="brand-name">tuchwelt.de</p><p class="brand-tagline">Stoffe für Wohnen, Hobby &amp; Design</p></div>
    <div class="url-row url-row--bottom"><span>www.tuchwelt.de</span><span class="sep">·</span><span>www.tuchwelt.de</span><span class="sep">·</span><span>www.tuchwelt.de</span><span class="sep">·</span><span>www.tuchwelt.de</span><span class="sep">·</span><span>www.tuchwelt.de</span><span class="sep">·</span><span>www.tuchwelt.de</span><span class="sep">·</span></div>
  </section>

  <p class="variant-label" style="top:690px">d)</p>
  <section class="tape tape--d" style="top:714px">
    <div class="url-row url-row--top"><span>www.tuchwelt.de</span><span class="sep">·</span><span>www.tuchwelt.de</span><span class="sep">·</span><span>www.tuchwelt.de</span><span class="sep">·</span><span>www.tuchwelt.de</span><span class="sep">·</span><span>www.tuchwelt.de</span><span class="sep">·</span><span>www.tuchwelt.de</span><span class="sep">·</span></div>
    <div class="brand"><span class="brand-square"></span><p class="brand-name">tuchwelt.de</p><p class="brand-tagline">Stoffe für Wohnen, Hobby &amp; Design</p></div>
    <div class="url-row url-row--bottom"><span>www.tuchwelt.de</span><span class="sep">·</span><span>www.tuchwelt.de</span><span class="sep">·</span><span>www.tuchwelt.de</span><span class="sep">·</span><span>www.tuchwelt.de</span><span class="sep">·</span><span>www.tuchwelt.de</span><span class="sep">·</span><span>www.tuchwelt.de</span><span class="sep">·</span></div>
  </section>

  <p class="variant-label" style="top:915px">e)</p>
  <section class="tape tape--e" style="top:938px">
    <div class="url-row url-row--top"><span>www.tuchwelt.de</span><span class="sep">·</span><span>www.tuchwelt.de</span><span class="sep">·</span><span>www.tuchwelt.de</span><span class="sep">·</span><span>www.tuchwelt.de</span><span class="sep">·</span><span>www.tuchwelt.de</span><span class="sep">·</span><span>www.tuchwelt.de</span><span class="sep">·</span></div>
    <div class="brand"><span class="brand-square"></span><p class="brand-name">tuchwelt.de</p><p class="brand-tagline">Stoffe für Wohnen, Hobby &amp; Design</p></div>
    <div class="url-row url-row--bottom"><span>www.tuchwelt.de</span><span class="sep">·</span><span>www.tuchwelt.de</span><span class="sep">·</span><span>www.tuchwelt.de</span><span class="sep">·</span><span>www.tuchwelt.de</span><span class="sep">·</span><span>www.tuchwelt.de</span><span class="sep">·</span><span>www.tuchwelt.de</span><span class="sep">·</span></div>
  </section>

</main>
</body>
</html>
```